Wine Bottle Lable

Want a unique, simple but elegant, label for a wine bottle. I want to use the letters "TWQ" in the design which is a moniker for my last name "Tallwidge". The letters TWQ do not have to be juxtaposed together so that it is recognizable, or they could be something like T-WG, WG-T, TGW T-WG-T, etc. The X could be totally separated from the NO, or otherwise. The wine is a white wine in a clear bottle. I need Adobe Illustrator files so I can add the wine varietal, year, alcohol content. The label should be 4" wide and 5" tall.

Colors

Designer to choose colors to be used in the design.

Requirements
Nice to have
• outstanding but simple graphics

```html
<!DOCTYPE html>
<html lang="en">
<head>
<meta charset="utf-8">
<title>TWQ Sauvignon Blanc Label</title>
<link href="https://fonts.googleapis.com/css2?family=Montserrat:wght@300;400&display=swap" rel="stylesheet">
<style>
  :root {
    --backdrop: #f5f5f5;
    --paper: #ffffff;
    --ink: #1d1d1b;
    --night: #1d1d1b;
    --night-ink: #f2f2f2;
    --gold: #c9a06a;
  }
  * { margin: 0; padding: 0; box-sizing: border-box; }
  html, body {
    width: 1200px; height: 1058px; overflow: hidden;
    background: var(--backdrop);
  }
  .canvas { position: relative; width: 1200px; height: 1058px; }
  svg text { font-family: "Montserrat", sans-serif; font-weight: 300; }

  .label {
    position: absolute; left: 658px; top: 393px;
    width: 484px; height: 605px;
    background: var(--paper);
    box-shadow: 0 3px 7px rgba(0,0,0,0.14);
  }
  .label text { fill: var(--ink); }
  .corner { fill: var(--gold); }
  .varietal { font-size: 16px; letter-spacing: 9px; }
  .volume { font-size: 30px; letter-spacing: 9px; font-weight: 400; }

  .badge__arc { font-size: 25px; letter-spacing: 7px; }
  .badge__name { font-size: 108px; letter-spacing: 20px; }

  .swatch {
    position: absolute; left: 777px; top: 48px;
    width: 247px; height: 293px;
    background: var(--night);
    box-shadow: 0 4px 8px rgba(0,0,0,0.28);
  }
  .swatch text { fill: var(--night-ink); }
</style>
</head>
<body>
<main class="canvas">
  <svg class="label" viewBox="0 0 484 605" aria-label="Front label">
    <defs>
      <path id="arc-top" d="M 120 307 A 122 122 0 0 1 364 307"/>
      <path id="arc-bottom" d="M 103 307 A 139 139 0 0 0 381 307"/>
    </defs>
    <polygon class="corner" points="12,12 29,12 12,29"/>
    <polygon class="corner" points="455,12 472,12 472,29"/>
    <polygon class="corner" points="12,576 12,593 29,593"/>
    <polygon class="corner" points="472,576 472,593 455,593"/>

    <text class="varietal" x="246" y="40" text-anchor="middle">sauvignon&#160;&#160;blanc</text>

    <g class="badge">
      <text class="badge__arc"><textPath href="#arc-top" startOffset="50%" text-anchor="middle">white wine</textPath></text>
      <text class="badge__name" x="252" y="345" text-anchor="middle">TWQ</text>
      <text class="badge__arc"><textPath href="#arc-bottom" startOffset="50%" text-anchor="middle">vintage 2019</textPath></text>
    </g>

    <text class="volume" x="246" y="581" text-anchor="middle">750 ml</text>
  </svg>

  <svg class="swatch" viewBox="0 0 247 293" aria-label="Dark brand card">
    <defs>
      <path id="card-arc-top" d="M -122 0 A 122 122 0 0 1 122 0"/>
      <path id="card-arc-bottom" d="M -139 0 A 139 139 0 0 0 139 0"/>
    </defs>
    <g class="badge" transform="translate(123 146) scale(0.457)">
      <text class="badge__arc"><textPath href="#card-arc-top" startOffset="50%" text-anchor="middle">white wine</textPath></text>
      <text class="badge__name" x="10" y="38" text-anchor="middle">TWQ</text>
      <text class="badge__arc"><textPath href="#card-arc-bottom" startOffset="50%" text-anchor="middle">vintage 2019</textPath></text>
    </g>
  </svg>
</main>
</body>
</html>
```